Webdesign für Energieagentur
Zielgruppe
Keltaris richtet sich derzeit als Energieagentur aus.
Neben Strom- und Gastarife für den privaten als auch gewerblichen Wechsel kümmern wir uns um industrielle LED Beleuchtung. Auf der Startseite sollte eine Übersicht der Leistungen* befinden. Durch 'Klick' kommt man auf die Themenseite.
*Leistungen
Strom- Gastarife für Privatkunden
Strom- Gastarife für Gewerbekunden
LED Hallenbeleuchtung
LED Straßenbeleuchtung
Intelligente LED Beleuchtung
Gerne bin ich bezüglich der Aufteilung für Vorschläge und Anregungen offen.
Zielgruppe u.a. private Haushalte, Geschäftsführer, Einkäufer, Werkstattleiter
Aufgabenstellung
Logo ist bereits vorhanden.
Das Thema Energie soll ersichtlich sein. Ggf auch Energie- und CO2 Reduzierung.
Farbschema ist frei wählbar, sowie auch die Schriftart.
3 Gesichter für Kundenstimmen sollten mit vorhanden sein.
Das Logo darf auch gerne anders angeordnet werden z.B. Kopf des Fuchses links vor dem Text.

```html
<!DOCTYPE html>
<html lang="de">
<head>
<meta charset="utf-8">
<title>Keltaris – Energieagentur</title>
<link rel="stylesheet" href="https://fonts.googleapis.com/css2?family=Montserrat:wght@400;500;600;700&display=swap">
<style>
:root{
  --navy:#17242e;
  --white:#ffffff;
  --panel:#f2f2f2;
  --card:#f5f5f5;
  --text-grey:#5a5a5a;
  --yellow:#fdbf2d;
  --yellow-field:#e1b03c;
  --ink:#1a1a1a;
}
*{box-sizing:border-box;margin:0;padding:0}
html,body{width:1200px;height:2310px;overflow:hidden}
body{position:relative;background:var(--navy);font-family:'Montserrat',sans-serif;color:var(--white)}
.abs{position:absolute}

.hero{left:0;top:0;width:1200px;height:626px;
  background:
    radial-gradient(ellipse 700px 60px at 40% 440px,rgba(255,190,90,.45),rgba(255,190,90,0) 70%),
    linear-gradient(180deg,#1d3550 0%,#2c5377 22%,#4b7896 40%,#8a8a86 52%,#e0733a 62%,#f28d35 67%,#4a3424 73%,#241e1b 84%,#121417 100%)}
.hero-side{left:720px;top:0;width:480px;height:626px;background:rgba(8,16,28,.62)}

.logo{left:99px;top:27px;display:flex;align-items:center;gap:10px;font-size:22px;font-weight:600;color:var(--white)}
.logo .mark{width:22px;height:22px;background:var(--white);border-radius:50%}
.nav{left:760px;top:33px;display:flex;gap:36px;font-size:11px;font-weight:600}
.icons{left:1044px;top:31px;display:flex;gap:22px}
.header-line{left:99px;top:79px;width:1002px;height:1px;background:rgba(255,255,255,.35)}

.hero-title{left:99px;top:258px;font-size:30px;font-weight:700;line-height:36px}
.offer{left:788px;top:210px;width:300px}
.offer h2{font-size:18px;font-weight:700;white-space:nowrap;margin-bottom:14px}
.offer p{font-size:11px;line-height:19px;font-weight:500}
.btn{display:inline-block;background:var(--yellow);color:var(--ink);font-size:8px;font-weight:600;width:109px;height:24px;line-height:24px;text-align:center}
.offer .btn{margin-top:24px}

.tabs{left:99px;top:469px;width:1002px;height:49px;display:flex;background:var(--white)}
.tab{flex:1;padding-left:30px;line-height:49px;font-size:13px;font-weight:500;color:#444;border-right:1px solid #eee;white-space:nowrap}
.tab.active{background:var(--panel)}
.features{left:99px;top:518px;width:1002px;height:272px;background:var(--panel)}
.feature{top:80px;width:232px;color:var(--text-grey)}
.feature h3{font-size:13px;font-weight:500;color:#444;margin-bottom:14px}
.feature p{font-size:11px;line-height:16.5px}

.teaser{top:928px;width:325px}
.teaser h3{font-size:19px;font-weight:700;height:49px;white-space:nowrap}
.teaser .media{height:298px;background:linear-gradient(160deg,#f5f5f5 0%,#e8e8e8 100%)}
.teaser p{font-size:11px;line-height:19px;font-weight:500;margin:36px 0 20px;width:290px;height:57px}

.contact{left:0;top:1566px;width:1200px;height:551px;background:var(--yellow);color:var(--ink)}
.contact .label{left:158px;top:114px;font-size:14px;font-weight:500}
.contact .rule{left:158px;top:143px;width:885px;height:1px;background:#8a6a18}
.contact h2{left:158px;top:200px;font-size:32px;line-height:38px;font-weight:700}
.field{background:var(--yellow-field);font-size:9px;color:#7a5e1c;padding-left:13px;line-height:50px;width:165px;height:50px}
.field.message{width:376px;height:174px;line-height:normal;padding-top:20px;padding-left:15px}
.send{left:953px;top:419px;display:flex;align-items:center;gap:22px;font-size:13px;font-weight:600}

.footer-logo{left:157px;top:2211px;display:flex;align-items:center;gap:8px;font-size:15px;font-weight:600}
.footer-logo .mark{width:16px;height:16px;background:var(--white);border-radius:50%}
.links{font-size:11px;line-height:24px;font-weight:500}
.address{font-size:11px;line-height:17px;font-weight:500}
</style>
</head>
<body>
  <div class="abs hero" role="img" aria-label="Nächtliches Stadtpanorama bei Abenddämmerung mit leuchtender Strassenbeleuchtung"></div>
  <div class="abs hero-side"></div>

  <div class="abs logo"><span class="mark"></span>keltaris</div>
  <nav class="abs nav"><span>Services</span><span>About</span><span>Contact</span></nav>
  <div class="abs icons">
    <svg width="16" height="16" viewBox="0 0 16 16" fill="none" stroke="#fff" stroke-width="1.4"><circle cx="6.5" cy="6.5" r="5"/><line x1="10.2" y1="10.2" x2="15" y2="15"/></svg>
    <svg width="17" height="14" viewBox="0 0 17 14" stroke="#fff" stroke-width="1.4"><line x1="0" y1="2" x2="17" y2="2"/><line x1="0" y1="7" x2="17" y2="7"/><line x1="0" y1="12" x2="17" y2="12"/></svg>
  </div>
  <div class="abs header-line"></div>

  <h1 class="abs hero-title">Entdecken Sie unsere<br>Angebote.</h1>
  <div class="abs offer">
    <h2>Jetzt kostenloses Angebot anfordern!</h2>
    <p>Wir vergleichen Strom- und Gastarife für Haushalte und Betriebe und planen effiziente LED Beleuchtung. So senken Sie Energiekosten und CO2-Ausstoss spürbar.</p>
    <span class="btn">ANFORDERN</span>
  </div>

  <div class="abs tabs">
    <div class="tab active">Privatkunden</div>
    <div class="tab">Gewerbekunden</div>
    <div class="tab">LED Beleuchtung</div>
    <div class="tab">Intelligente LED</div>
  </div>
  <div class="abs features">
    <div class="abs feature" style="left:58px"><h3>Schnell</h3><p>Ihr Wechsel zu einem günstigeren Strom- oder Gastarif ist in wenigen Minuten erledigt. Wir übernehmen Kündigung und Anmeldung beim neuen Anbieter für Sie.</p></div>
    <div class="abs feature" style="left:385px"><h3>Wirtschaftlich</h3><p>Durch passende Tarife und sparsame LED Technik sinken Ihre Energiekosten dauerhaft. Gleichzeitig reduzieren Sie Ihren Verbrauch und den CO2-Ausstoss.</p></div>
    <div class="abs feature" style="left:712px"><h3>Temporär</h3><p>Sie bleiben flexibel: kurze Vertragslaufzeiten und jährliche Prüfung Ihrer Tarife. Wir melden uns, sobald es ein besseres Angebot für Sie gibt.</p></div>
  </div>

  <div class="abs teaser" style="left:99px"><h3>Hallenbeleuchtung</h3><div class="media" role="img" aria-label="Kundenportrait: Werkstattleiter eines Metallbaubetriebs"></div><p>«Seit der Umrüstung auf LED ist unsere Halle heller und der Stromverbrauch um 60 % gesunken.» – Metallbau Krämer</p><span class="btn">mehr erfahren</span></div>
  <div class="abs teaser" style="left:437px"><h3>Strassenbeleuchtung</h3><div class="media" role="img" aria-label="Kundenportrait: Einkäuferin einer Gemeinde"></div><p>«Die neuen LED Leuchten sparen unserer Gemeinde jedes Jahr Energie und viele Tonnen CO2.» – Gemeinde Talwil</p><span class="btn">mehr erfahren</span></div>
  <div class="abs teaser" style="left:776px"><h3>Strom- und Gastarife</h3><div class="media" role="img" aria-label="Kundenportrait: Privatkundin zu Hause"></div><p>«Der Tarifwechsel war völlig unkompliziert und wir zahlen nun deutlich weniger für Strom.» – Familie Berger</p><span class="btn">mehr erfahren</span></div>

  <section class="abs contact">
    <div class="abs label">Kontaktformular</div>
    <div class="abs rule"></div>
    <h2 class="abs">Wie können wir<br>Ihnen helfen?</h2>
    <div class="abs field" style="left:483px;top:201px">Name</div>
    <div class="abs field" style="left:483px;top:263px">E-Mail</div>
    <div class="abs field" style="left:483px;top:325px">Telefon</div>
    <div class="abs field message" style="left:667px;top:201px">Ihre Nachricht</div>
    <div class="abs send">Senden
      <svg width="18" height="16" viewBox="0 0 18 16"><path d="M0 0 L18 8 L0 16 L4 8 Z" fill="#1a1a1a"/></svg>
    </div>
  </section>

  <div class="abs footer-logo"><span class="mark"></span>keltaris</div>
  <div class="abs links" style="left:309px;top:2184px">Services<br>About<br>Contact</div>
  <div class="abs links" style="left:386px;top:2184px">Impressum<br>AGB<br>Datenschutz</div>
  <div class="abs address" style="left:805px;top:2195px">Max Muster<br>Musterstrasse 20<br>3000 Musterhausen</div>
  <div class="abs address" style="left:952px;top:2194px">info@keltaris.ch<br>031 456 78 90</div>
</body>
</html>
```